Design us a professional website for a Cannabis Staffing Agency

We already have a logo ready to go, but now we are looking for a few good web designs. We provide staffing for the Cannabis/Marijuana industry. We want a good balance of clean, simple and modern design but also embracing the exciting atmosphere of the Cannabis industry.

Here are examples of our competition, please note that most of these competitors design feel old and dated:

http://qrvplacementcrew.example/
https://tolbrix.example/tolbrix-main-page
http://saffronpathways.example/index.html
http://www.wickcrew.example/medical-marijuana-staffing-recruiting
http://www.tundrahiring.example/
www.placedupcrew.example
www.pinewise.example

I also would prefer an explanation of why you choose to design it the way you did? What was your thought process or did you use a template?

Requirements
Must have
• About Us Page
• Candidates Page
• Employer Page
• Job Opening Page
• Contact Us Page
Nice to have
• Colors to match the logo, good use of images and design to show the story. Our goal is to show our clients what we are about and not just tell them.

```html
<!DOCTYPE html>
<html lang="en">
<head>
<meta charset="utf-8">
<title>VERDALINK – Cannabis Staffing</title>
<link href="https://fonts.googleapis.com/css2?family=Montserrat:wght@400;500;600;700&family=Open+Sans:wght@400;600&display=swap" rel="stylesheet">
<style>
:root{
  --green:#6f9f1c;
  --green-light:#8dbb2e;
  --dark:#151515;
  --ink:#1d1d1d;
  --muted:#555;
  --grey:#5a5a5a;
  --field:#eef0ee;
  --field-line:#9a9a9a;
}
*{margin:0;padding:0;box-sizing:border-box}
html,body{width:1200px;height:4390px;overflow:hidden}
body{position:relative;background:#fff;font-family:"Open Sans",Arial,sans-serif;color:var(--ink)}
.abs{position:absolute}
.center{text-align:center}

/* header */
.site-header{left:0;top:0;width:1200px;height:111px;background:var(--dark)}
.brand{left:79px;top:22px;display:flex;align-items:center;gap:14px}
.brand-dot{width:62px;height:62px;border-radius:50%;background:var(--green)}
.brand-text{font-family:"Montserrat",sans-serif;color:var(--green-light)}
.brand-name{font-size:38px;font-weight:600;line-height:1;letter-spacing:1px}
.brand-tag{font-size:9px;font-weight:600;letter-spacing:1px;margin-top:3px}
.main-nav{left:462px;top:34px;display:flex;gap:8px;font-family:"Montserrat",sans-serif;font-size:14px}
.main-nav a{color:#ddd;text-decoration:none;padding:10px 16px;border:1px solid transparent}
.main-nav a.active{color:var(--green-light);border-color:var(--green-light)}

/* photo fills */
.hero-photo{left:0;top:111px;width:1200px;height:1530px;
  background:linear-gradient(180deg,rgba(255,255,255,0) 70%,#fff 100%),linear-gradient(90deg,#9fb590 0%,#e8eee4 20%,#f7f8f6 50%,#e4ebdf 80%,#98ae88 100%)}
.foot-photo{left:0;top:3366px;width:1200px;height:849px;
  background:linear-gradient(180deg,#fff 0%,rgba(255,255,255,0) 30%),linear-gradient(90deg,#8fa97f 0%,#e9eee6 22%,#f8f9f7 50%,#e5ece0 78%,#90a880 100%)}

/* hero */
.hero-title{left:79px;top:298px;font-family:"Montserrat",sans-serif;font-weight:600;font-size:28px;letter-spacing:1px;color:var(--ink)}
.hero-title b{font-size:46px;font-weight:600}
.hero-sub{left:79px;top:360px;font-family:"Montserrat",sans-serif;font-weight:600;font-size:48px;color:var(--green)}
.btn{display:inline-block;border:2px solid var(--ink);background:#fff;font-family:"Montserrat",sans-serif;font-size:18px;color:var(--ink);text-align:center;text-decoration:none}
.hero-btns{left:79px;top:448px;display:flex;gap:8px}
.hero-btns .btn{width:190px;height:56px;line-height:52px}
.chevron{width:36px;height:30px}

/* about */
.h2{font-family:"Montserrat",sans-serif;font-weight:500;font-size:50px;color:var(--ink)}
.lead{font-size:14px;line-height:22px;color:var(--muted)}
.feature-icon{width:146px;height:146px;border-radius:50%;border:4px solid var(--green-light);background:radial-gradient(circle,#fff 55%,#e8f0dc 100%)}
.feature-title{font-family:"Montserrat",sans-serif;font-weight:600;font-size:20px;letter-spacing:1px;color:var(--ink)}
.feature-text{width:290px;font-size:14.5px;line-height:23px;color:var(--muted)}

/* audience */
.round-photo{border-radius:50%;border:3px solid #444}
.aud-title{font-family:"Montserrat",sans-serif;font-size:26px;color:var(--ink)}
.aud-text{width:340px;font-size:14px;line-height:22px;color:var(--muted)}
.small-btn{width:144px;height:44px;line-height:40px;font-size:14px}
.rule{background:var(--green)}

/* testimonial */
.quote{font-family:Georgia,serif;font-size:110px;line-height:1;color:#c2d59a}
.testimonial{left:220px;top:2546px;width:760px;font-style:italic;font-size:15px;line-height:24px;color:var(--muted)}
.testimonial-name{left:0;top:2630px;width:1200px;font-family:"Montserrat",sans-serif;font-size:20px;color:var(--green)}

/* career form */
.career-title{left:79px;top:2960px;font-family:"Open Sans",sans-serif;font-weight:400;font-size:48px;color:var(--ink)}
.field{background:var(--field);border:1.5px solid var(--field-line);font-size:14px;color:#333;padding:12px 14px}
.submit{background:#000;color:#fff;font-family:"Montserrat",sans-serif;font-size:20px;text-align:center;line-height:50px}
.dots-btn{background:var(--field);border:1.5px solid var(--field-line);display:flex;align-items:center;justify-content:center;gap:7px}
.dots-btn i{width:9px;height:9px;border-radius:50%;background:var(--green)}
.desk-photo{left:690px;top:2890px;width:510px;height:470px;background:radial-gradient(ellipse at 55% 45%,#e2e5e0 0%,#eef0ed 40%,rgba(255,255,255,0) 70%)}

/* news */
.news{display:flex;gap:16px;width:340px}
.date{width:79px;flex:none}
.date-day{height:58px;background:var(--green);color:#fff;font-family:"Montserrat",sans-serif;font-size:36px;text-align:center;line-height:58px}
.date-month{height:54px;background:var(--grey);color:#fff;font-size:18px;text-align:center;line-height:54px}
.news-title{font-size:18px;color:var(--ink);margin-top:4px}
.news-text{font-size:14px;line-height:19px;color:var(--muted);margin-top:6px}
.news-link{font-size:13px;color:var(--ink);text-decoration:underline;margin-top:6px;display:block}

/* updates */
.update-btn{width:176px;height:52px;line-height:48px;font-size:18px}

/* footer */
.site-footer{left:0;top:4215px;width:1200px;height:175px;background:var(--dark)}
.social{left:222px;top:4236px;display:flex;gap:10px}
.social i{width:40px;height:40px;border-radius:50%;background:#fff;display:block}
.copy{left:92px;top:4300px;font-size:13px;line-height:21px;color:#bbb;text-align:center;width:330px}
.copy b{color:var(--green-light);font-weight:600}
.foot-brand{left:494px;top:4262px}
.contact{left:868px;top:4242px;font-size:14px;line-height:21px;color:#eee}
.contact li{list-style:none;display:flex;gap:16px;align-items:flex-start;margin-bottom:10px}
.contact svg{flex:none;margin-top:3px}
</style>
</head>
<body>

<div class="abs hero-photo" role="img" aria-label="Bright greenhouse interior with cactus and succulent plants"></div>
<div class="abs foot-photo" role="img" aria-label="Greenhouse rows of potted cactus and plants"></div>

<header class="abs site-header">
  <div class="abs brand">
    <span class="brand-dot"></span>
    <div class="brand-text">
      <div class="brand-name">VERDALINK</div>
      <div class="brand-tag">GROW YOUR CANNABIS CAREER</div>
    </div>
  </div>
  <nav class="abs main-nav">
    <a class="active" href="#">HOME</a>
    <a href="#">ABOUT US</a>
    <a href="#">CANDIDATES</a>
    <a href="#">EMPLOYER</a>
    <a href="#">CAREER</a>
    <a href="#">CONTACT US</a>
  </nav>
</header>

<section>
  <div class="abs hero-title">LOOKING FOR A <b>BETTER SOLUTION</b></div>
  <div class="abs hero-sub">For your STAFFING?</div>
  <div class="abs hero-btns">
    <a class="btn" href="#">JOIN NOW</a>
    <a class="btn" href="#">LEARN MORE</a>
  </div>
  <svg class="abs chevron" style="left:582px;top:638px" viewBox="0 0 36 30"><path d="M4 3l14 10 14-10M4 15l14 10 14-10" fill="none" stroke="#5c8a12" stroke-width="6"/></svg>
</section>

<section>
  <h2 class="abs h2 center" style="left:0;top:810px;width:1200px">About VERDALINK</h2>
  <p class="abs lead center" style="left:200px;top:892px;width:800px">Lorem ipsum dolor sit amet, consectetur adipiscing elit. Etiam vehicula tincidunt dictum. Suspendisse sollicitudin est in eros ultrices, vel hendrerit nulla pharetra. Fusce nec rhoncus enim. Mauris sit dictum velit, et placerat lorem.Lorem ipsum dolor sit amet, consectetur adipiscing elit. Etiam vehicula tincidunt dictum. Suspendisse sollicitudin est in eros ultrices, vel hendrerit nulla pharetra. Fusce nec rhoncus enim. Mauris id dictum velit, et placerat lorem.</p>

  <div class="abs feature-icon" style="left:328px;top:1000px"></div>
  <svg class="abs" style="left:362px;top:1035px" width="78" height="78" viewBox="0 0 78 78"><circle cx="28" cy="28" r="13" fill="#555"/><circle cx="50" cy="34" r="13" fill="#444"/><path d="M6 62c0-14 10-22 22-22s18 6 20 14H6z" fill="#555"/><path d="M26 70c0-14 11-22 24-22s24 8 24 22z" fill="#444"/></svg>
  <div class="abs feature-title center" style="left:250px;top:1170px;width:300px">QUALITY STAFFING</div>
  <p class="abs feature-text center" style="left:255px;top:1204px">Lorem ipsum dolor sit amet, consectetur adipiscing elit. Etiam vehicula tincidunt dictum. Suspendisse sollicitudin est in eros ultrices, vel hendrerit nulla pharetra.</p>

  <div class="abs feature-icon" style="left:723px;top:1000px"></div>
  <svg class="abs" style="left:776px;top:1030px" width="40" height="86" viewBox="0 0 40 86"><path d="M20 2c10 10 13 24 12 44H8C7 26 10 12 20 2z" fill="#444"/><path d="M8 42L0 60h8zM32 42l8 18h-8z" fill="#444"/><path d="M14 50h12l-6 14z" fill="#666"/></svg>
  <div class="abs feature-title center" style="left:646px;top:1170px;width:300px">RECRUITING</div>
  <p class="abs feature-text center" style="left:650px;top:1204px">Lorem ipsum dolor sit amet, consectetur adipiscing elit. Etiam vehicula tincidunt dictum. Suspendisse sollicitudin est in eros ultrices, vel hendrerit nulla pharetra.</p>

  <svg class="abs chevron" style="left:582px;top:1372px" viewBox="0 0 36 30"><path d="M4 3l14 10 14-10M4 15l14 10 14-10" fill="none" stroke="#5c8a12" stroke-width="6"/></svg>
</section>

<section>
  <div class="abs round-photo" style="left:106px;top:1634px;width:280px;height:280px;background:linear-gradient(160deg,#3a3f47,#15181d)" role="img" aria-label="Group of young candidates in dark jackets"></div>
  <div class="abs rule" style="left:138px;top:1790px;width:3px;height:120px"></div>
  <div class="abs aud-title center" style="left:46px;top:1940px;width:400px">For Candidate</div>
  <p class="abs aud-text center" style="left:76px;top:1984px">Lorem ipsum dolor sit amet, consectetur adipiscing elit. Etiam vehicula tincidunt dictum. Suspendisse sollicitudin est in eros ultrices, vel hendrerit nulla pharetra. Fusce nec rhoncus enim.</p>
  <a class="abs btn small-btn" style="left:172px;top:2090px" href="#">LEARN MORE</a>

  <div class="abs aud-title center" style="left:400px;top:1688px;width:400px">For Employee</div>
  <div class="abs rule" style="left:710px;top:1707px;width:118px;height:3px"></div>
  <p class="abs aud-text center" style="left:430px;top:1732px">Lorem ipsum dolor sit amet, consectetur adipiscing elit. Etiam vehicula tincidunt dictum. Suspendisse sollicitudin est in eros ultrices.</p>
  <a class="abs btn small-btn" style="left:528px;top:1816px" href="#">LEARN MORE</a>

  <div class="abs round-photo" style="left:819px;top:1636px;width:276px;height:276px;background:linear-gradient(160deg,#d9dde0,#7a818a)" role="img" aria-label="Business people shaking hands in an office"></div>

  <div class="abs round-photo" style="left:460px;top:1856px;width:280px;height:280px;background:linear-gradient(160deg,#e7e1da,#6f6760)" role="img" aria-label="Smiling professional woman at a laptop"></div>
  <div class="abs rule" style="left:660px;top:1950px;width:200px;height:3px"></div>
  <div class="abs aud-title center" style="left:756px;top:1930px;width:400px">For Career</div>
  <p class="abs aud-text center" style="left:786px;top:1974px">Lorem ipsum dolor sit amet, consectetur adipiscing elit. Etiam vehicula tincidunt dictum. Suspendisse sollicitudin est in eros ultrices, vel hendrerit nulla pharetra. Fusce nec rhoncus enim.</p>
  <a class="abs btn small-btn" style="left:880px;top:2080px" href="#">LEARN MORE</a>

  <svg class="abs chevron" style="left:582px;top:2248px" viewBox="0 0 36 30"><path d="M4 3l14 10 14-10M4 15l14 10 14-10" fill="none" stroke="#5c8a12" stroke-width="6"/></svg>
</section>

<section>
  <div class="abs" style="left:550px;top:2423px;width:100px;height:100px;border-radius:50%;border:3px solid #ddd;background:linear-gradient(160deg,#e8c8a8,#b08a68)" role="img" aria-label="Client portrait"></div>
  <div class="abs quote" style="left:118px;top:2530px">&ldquo;</div>
  <div class="abs quote" style="left:1022px;top:2530px">&rdquo;</div>
  <p class="abs testimonial center">Lorem ipsum dolor sit amet, consectetur adipiscing elit, sed do eiusmod tempor incididunt ut labore et dolore magna aliqua. Ut enim ad minim veniam, quis nostrud exercitation ullamco laboris nisi ut aliquip ex ea commodo consequat.Lorem ipsum dolor sit amet, consectetur adipiscing elit, sed do eiusmod tempor incididunt .</p>
  <div class="abs testimonial-name center">Lorem Ipsum</div>
  <svg class="abs chevron" style="left:582px;top:2804px" viewBox="0 0 36 30"><path d="M4 3l14 10 14-10M4 15l14 10 14-10" fill="none" stroke="#5c8a12" stroke-width="6"/></svg>
</section>

<section>
  <div class="abs desk-photo" role="img" aria-label="Desk with succulent pot, notebook with growth sketch and green pen"></div>
  <h2 class="abs career-title">Your CAREER With US</h2>
  <div class="abs field" style="left:79px;top:3082px;width:293px;height:50px">Name *</div>
  <div class="abs field" style="left:380px;top:3082px;width:296px;height:50px">Email Id *</div>
  <div class="abs field" style="left:79px;top:3138px;width:597px;height:98px">Message *</div>
  <div class="abs field" style="left:79px;top:3249px;width:293px;height:50px">File...</div>
  <div class="abs dots-btn" style="left:380px;top:3249px;width:109px;height:50px"><i></i><i></i><i></i></div>
  <div class="abs submit" style="left:498px;top:3249px;width:178px;height:50px">SUBMIT</div>
</section>

<section>
  <div class="abs news" style="left:79px;top:3547px">
    <div class="date"><div class="date-day">05</div><div class="date-month">May</div></div>
    <div><div class="news-title">Lorem ipsum dolor sit amet</div><div class="news-text">Lorem ipsum dolor sit amet, consectetur adipiscing elit</div><span class="news-link">READ MORE</span></div>
  </div>
  <div class="abs news" style="left:442px;top:3547px">
    <div class="date"><div class="date-day">05</div><div class="date-month">May</div></div>
    <div><div class="news-title">Lorem ipsum dolor sit amet</div><div class="news-text">Lorem ipsum dolor sit amet, consectetur adipiscing elit</div><span class="news-link">READ MORE</span></div>
  </div>
  <div class="abs news" style="left:805px;top:3547px">
    <div class="date"><div class="date-day">05</div><div class="date-month">May</div></div>
    <div><div class="news-title">Lorem ipsum dolor sit.</div><div class="news-text">Lorem ipsum dolor sit amet, consectetur adipiscing elit</div><span class="news-link">READ MORE</span></div>
  </div>
</section>

<section>
  <h2 class="abs h2 center" style="left:0;top:3798px;width:1200px">Keep ME Updated</h2>
  <p class="abs lead center" style="left:200px;top:3882px;width:800px;font-size:14.5px;line-height:22px">Lorem ipsum dolor sit amet, consectetur adipiscing elit, sed do eiusmod tempor incididunt ut labore et dolore magna aliqua. Ut enim ad minim veniam, quis nostrud exercitation ullamco laboris nisi ut aliquip ex ea commodo consequat.Lorem ipsum dolor sit amet, consectetur adipiscing elit.</p>
  <a class="abs btn update-btn" style="left:512px;top:3966px" href="#">GET STARTED</a>
</section>

<footer class="abs site-footer"></footer>
<div class="abs social" aria-label="Social links"><i></i><i></i><i></i><i></i></div>
<p class="abs copy">&copy; <b>VERDALINK Grow Your Cannabis Career</b><br>- 2017. All Rights reserved.</p>
<div class="abs brand foot-brand">
  <span class="brand-dot" style="width:70px;height:70px"></span>
  <div class="brand-text">
    <div class="brand-name" style="font-size:40px">VERDALINK</div>
    <div class="brand-tag">GROW YOUR CANNABIS CAREER</div>
  </div>
</div>
<ul class="abs contact">
  <li><svg width="16" height="20" viewBox="0 0 16 20"><path d="M8 0a8 8 0 00-8 8c0 6 8 12 8 12s8-6 8-12a8 8 0 00-8-8z" fill="#fff"/><circle cx="8" cy="8" r="3" fill="#151515"/></svg><span>Lorem ipsum dolor sit amet,<br>conse ctetur adipiscing elit.</span></li>
  <li><svg width="16" height="16" viewBox="0 0 16 16"><path d="M3 0l3 4-2 2c1 3 3 5 6 6l2-2 4 3-2 3C7 16 0 9 0 2z" fill="#fff"/></svg><span>555 014 2290</span></li>
  <li><svg width="16" height="12" viewBox="0 0 16 12"><rect width="16" height="12" fill="#fff"/><path d="M0 0l8 6 8-6" fill="none" stroke="#151515" stroke-width="1.5"/></svg><span>info@verdalinkcareer.example</span></li>
</ul>

</body>
</html>
```